512 Calloway Label for our FIRST product!!!!!

The name of the company is "512 Calloway", the tagline is "Where Glow Begins", the product is Leave in Conditioner. This is a product that can be used for men and women, but our target market is 20-40 year old women, strictly for online sales. I need a label design that will fit an 8oz pump bottle(4H by 6W dieline) and a 2oz pump bottle(4.25H by 2,25W dueling), the dielines are attached. The bottle will be white, the spray top will be black on both the 2oz and 8oz bottles. The four photos of Vel Maison are examples of how I want the bottles to look. Ingredients, symbols and UPC need to be on the side of the bottle. Logo has to be in the middle, name of the product on the bottom (logo is attached). I do not have a UPC yet so I added a copied image. Some of the ingredients, symbols and UPC will eventually change. Even though I have an idea of what I want, please feel free to give me your opinion. This is one of ten products the will be launched under this label.

Target Market(s)

This is a product that can be used for men and women, but our target market is 20-40 year old women, strictly for online sales.

Industry/Entity Type

Hair And Beauty

Font styles to use
Other font styles liked:
• Numbers are Lemon/Milk, font is steelfish

Colors
1b1b1b
5c5c5c
aaaaaa

Requirements
Must have
• I need a label design that will fit an 8oz pump bottle(4H by 6W dieline) and a 2oz pump bottle(4.25H by 2,25W dueling), the dielines are attached.
Nice to have
• Logo has to be in the middle, name of the product on the bottom (logo is attached). I do not have a UPC yet so I added a copied image. Some of the ingredients, symbols and UPC will eventually change.

```html
<!DOCTYPE html>
<html lang="en">
<head>
<meta charset="utf-8">
<title>512 Calloway — Leave in Conditioner Label, 2oz</title>
<link rel="stylesheet" href="https://fonts.googleapis.com/css2?family=Montserrat:wght@500;700&family=Oswald:wght@300&display=swap">
<style>
  :root {
    --ink: #1b1b1b;
    --mid: #5c5c5c;
    --soft: #aaaaaa;
    --paper: #ffffff;
    --backdrop: #ffffff;
  }
  html, body {
    margin: 0;
    padding: 0;
    width: 1200px;
    height: 1200px;
    overflow: hidden;
    background: var(--backdrop);
  }
  .canvas {
    position: relative;
    width: 1200px;
    height: 1200px;
  }
  .label {
    position: absolute;
    left: 477px;
    top: 136px;
    width: 246px;
    height: 927px;
  }
  .label-sheet { fill: var(--paper); stroke: #e4e4e4; stroke-width: 1; }
  .brand-band { fill: var(--ink); }
  .logo-box { fill: var(--ink); }
  .logo-rule { fill: none; stroke: var(--paper); stroke-width: 1.5; }
  .brand-name {
    font-family: "Montserrat", sans-serif;
    font-weight: 500;
    font-size: 21px;
    letter-spacing: 0.5px;
    fill: var(--paper);
  }
  .brand-tagline {
    font-family: "Montserrat", sans-serif;
    font-weight: 500;
    font-size: 8px;
    letter-spacing: 1px;
    fill: var(--soft);
  }
  .product-type {
    font-family: "Oswald", sans-serif;
    font-weight: 300;
    font-size: 25px;
    fill: var(--paper);
  }
  .product-name {
    font-family: "Montserrat", sans-serif;
    font-weight: 700;
    font-size: 32px;
    fill: var(--ink);
  }
  .volume {
    font-family: "Montserrat", sans-serif;
    font-weight: 500;
    font-size: 23px;
    fill: var(--ink);
  }
</style>
</head>
<body>
<main class="canvas">
  <svg class="label" viewBox="0 0 246 927" xmlns="http://www.w3.org/2000/svg" aria-label="512 Calloway Leave in Conditioner, 2oz label">
    <rect class="label-sheet" x="0.5" y="0.5" width="245" height="926"/>

    <rect class="brand-band" x="88" y="70" width="60" height="857"/>

    <g class="logo">
      <rect class="logo-box" x="35" y="153" width="174" height="174" rx="6"/>
      <rect class="logo-rule" x="39" y="157" width="166" height="166" rx="4"/>
      <text class="brand-name" x="122" y="246" text-anchor="middle">512 Calloway</text>
      <text class="brand-tagline" x="122" y="272" text-anchor="middle">WHERE GLOW BEGINS</text>
    </g>

    <text class="product-type" transform="translate(139 810) rotate(-90)">Leave in</text>
    <text class="product-name" transform="translate(200 810) rotate(-90)">CONDITIONER</text>

    <text class="volume" x="24" y="878">2oz</text>
  </svg>
</main>
</body>
</html>
```